Design for Training Manuals

We need a graphic design for new training manuals for our organization called Lanternfield Trust, Inc. We are a children's rights NGO based in the Philippines. We are running an advocacy campaign called Raise Every Voice which advocates for the prevention of child sexual abuse and sexual exploitation of children. The Raise Every Voice Campaign is gaining momentum in various countries around the world and we would like to provide our constituents with inspiring training materials that will enable them to carry out the work of protecting children's rights.
Because of the sensitive nature of the subject matter, we would like to present a non-threatening light design, with a creative edge, that incorporates our Raise Every Voice logo. Also, I have attached an image from which you can design from.
Please feel free to visit our website for inspiration: www.lanternfieldtrust.org
Updates
Dear Designers,
I am excited about this project. I have uploaded a couple of our training modules. Overall there are 2 levels: Level 1 with 3 training modules and Level 2 also with 3 training modules.
Thank you,
Delia
Target Market(s)
Non-government workers, government workers, teachers, social workers...
Industry/Entity Type
Graphic Design
Look and feel
Each slider illustrates characteristics of the customer's brand and the style your logo design should communicate.

```html
<!DOCTYPE html>
<html lang="en">
<head>
<meta charset="utf-8">
<title>Raise Every Voice – Training Manual Design</title>
<link rel="stylesheet" href="https://fonts.googleapis.com/css2?family=Crimson+Pro:wght@400;600&family=Arimo:wght@700&display=swap">
<style>
  :root {
    --frame-grey: #99999e;
    --page-white: #ffffff;
    --ink: #4a4a4a;
    --ink-soft: #6a6a6a;
    --rule: #b8b8b8;
    --placeholder: #d3d3d3;
    --orange: #e0a028;
    --cyan: #22c0e0;
    --red: #e33a27;
    --pink: #e088bf;
    --green: #86c96a;
    --brand: #b8322b;
  }
  * { box-sizing: border-box; margin: 0; padding: 0; }
  html, body { width: 1200px; height: 854px; overflow: hidden; background: var(--page-white); }
  body { position: relative; font-family: "Crimson Pro", Georgia, serif; color: var(--ink); }

  .cover-frame { position: absolute; left: 0; top: 0; width: 582px; height: 823px; background: var(--frame-grey); }
  .cover { position: absolute; left: 10px; top: 10px; width: 562px; height: 800px; background: var(--page-white); }

  .brand { position: absolute; left: 60px; top: 62px; }
  .brand-name { display: flex; align-items: center; gap: 8px; font-size: 36px; font-weight: 600; color: var(--brand); line-height: 1; }
  .brand-dot { width: 14px; height: 14px; border-radius: 50%; background: var(--orange); }
  .brand-tagline { margin-top: 8px; font-family: "Arimo", Arial, sans-serif; font-weight: 700; font-size: 9.6px; color: #222; }

  .tile { position: absolute; width: 144px; height: 144px; }
  .tile-orange { left: 378px; top: 242px; background: var(--orange); }
  .tile-cyan { left: 60px; top: 400px; background: var(--cyan); }
  .tile-art { left: 218px; top: 400px; background: linear-gradient(135deg, #f2c84a 0%, #e9705a 35%, #8fb7e0 65%, #f4e3c8 100%); }
  .tile-red { left: 378px; top: 400px; background: var(--red); }
  .tile-pink { left: 60px; top: 558px; background: var(--pink); }
  .tile-green { left: 218px; top: 558px; background: var(--green); }

  .cover-line { position: absolute; color: var(--ink); line-height: 1.1; }
  .best-interest { left: 218px; top: 344px; font-size: 17px; }
  .best-interest .big { font-size: 25px; }
  .rights-now { left: 378px; top: 646px; font-size: 19px; }
  .rights-now .big { display: block; font-size: 33px; }
  .survival { left: 62px; top: 562px; color: var(--page-white); font-size: 26px; }
  .survival .small { display: block; font-size: 16px; margin-top: 4px; }

  .inside { position: absolute; left: 618px; top: 0; width: 582px; height: 823px; border: 1px solid var(--rule); border-right: none; background: var(--page-white); }
  .color-bar { position: absolute; left: 364px; top: 47px; width: 218px; height: 9px; display: flex; }
  .color-bar span { flex: 1; }
  .heading-small { position: absolute; left: 33px; top: 44px; font-size: 20px; color: var(--ink-soft); }
  .heading-large { position: absolute; left: 33px; top: 64px; font-size: 35px; color: var(--ink-soft); }

  .body-text { position: absolute; left: 33px; font-size: 10.2px; line-height: 13.8px; color: var(--ink-soft); overflow: hidden; }
  .para-intro { top: 125px; width: 506px; height: 70px; }
  .para-side { top: 222px; width: 318px; height: 112px; }
  .para-three { top: 401px; width: 506px; height: 70px; }
  .para-four { top: 482px; width: 506px; height: 70px; }
  .image-slot { position: absolute; background: var(--placeholder); }
  .slot-side { left: 372px; top: 223px; width: 179px; height: 132px; }
  .slot-wide { left: 33px; top: 564px; width: 518px; height: 236px; }
  .divider { position: absolute; left: 33px; top: 373px; width: 518px; height: 1px; background: var(--rule); }

  .caption { position: absolute; top: 822px; font-size: 22px; color: var(--ink); text-align: center; }
  .caption-cover { left: 0; width: 582px; }
  .caption-inside { left: 618px; width: 582px; }
</style>
</head>
<body>
  <div class="cover-frame">
    <section class="cover">
      <div class="brand">
        <div class="brand-name"><span class="brand-dot"></span>Raise Every Voice</div>
        <div class="brand-tagline">Stop child sexual abuse and exploitation</div>
      </div>
      <div class="cover-line best-interest">In The Best Interest<br>Of the <span class="big">Child</span></div>
      <div class="tile tile-orange"></div>
      <div class="tile tile-cyan"></div>
      <div class="tile tile-art" role="img" aria-label="Colourful illustration of a crowd of children holding placards"></div>
      <div class="tile tile-red"></div>
      <div class="tile tile-pink"></div>
      <div class="tile tile-green"></div>
      <div class="cover-line survival">Survival<span class="small">&amp; development</span></div>
      <div class="cover-line rights-now">Children’s rights<span class="big">Now!</span></div>
    </section>
  </div>

  <section class="inside">
    <div class="color-bar">
      <span style="background:var(--orange)"></span><span style="background:var(--red)"></span><span style="background:var(--green)"></span><span style="background:var(--pink)"></span><span style="background:var(--cyan)"></span>
    </div>
    <div class="heading-small">Heading</div>
    <div class="heading-large">Heading</div>
    <p class="body-text para-intro">Dummy text Dummy text Dummy text Dummy text Dummy text Dummy text Dummy text Dummy text Dummy text Dummy text Dummy text Dummy text Dummy text Dummy text Dummy text Dummy text Dummy text Dummy text Dummy text Dummy text Dummy text Dummy text Dummy text Dummy text Dummy text Dummy text Dummy text Dummy text Dummy text Dummy text Dummy text Dummy text Dummy text Dummy text Dummy text Dummy text Dummy text Dummy text Dummy text Dummy text Dummy text Dummy text Dummy text Dummy text Dummy text Dummy text Dummy text Dummy text Dummy text Dummy text Dummy text</p>
    <p class="body-text para-side">Dummy text Dummy text Dummy text Dummy text Dummy text Dummy text Dummy text Dummy text Dummy text Dummy text Dummy text Dummy text Dummy text Dummy text Dummy text Dummy text Dummy text Dummy text Dummy text Dummy text Dummy text Dummy text Dummy text Dummy text Dummy text Dummy text Dummy text Dummy text Dummy text Dummy text Dummy text Dummy text Dummy text Dummy text Dummy text Dummy text Dummy text Dummy text Dummy text Dummy text Dummy text Dummy text Dummy text Dummy text Dummy text Dummy text Dummy text</p>
    <div class="image-slot slot-side" role="img" aria-label="Image placeholder"></div>
    <div class="divider"></div>
    <p class="body-text para-three">Dummy text Dummy text Dummy text Dummy text Dummy text Dummy text Dummy text Dummy text Dummy text Dummy text Dummy text Dummy text Dummy text Dummy text Dummy text Dummy text Dummy text Dummy text Dummy text Dummy text Dummy text Dummy text Dummy text Dummy text Dummy text Dummy text Dummy text Dummy text Dummy text Dummy text Dummy text Dummy text Dummy text Dummy text Dummy text Dummy text Dummy text Dummy text Dummy text Dummy text Dummy text Dummy text Dummy text Dummy text Dummy text Dummy text</p>
    <p class="body-text para-four">Dummy text Dummy text Dummy text Dummy text Dummy text Dummy text Dummy text Dummy text Dummy text Dummy text Dummy text Dummy text Dummy text Dummy text Dummy text Dummy text Dummy text Dummy text Dummy text Dummy text Dummy text Dummy text Dummy text Dummy text Dummy text Dummy text Dummy text Dummy text Dummy text Dummy text Dummy text Dummy text Dummy text Dummy text Dummy text Dummy text Dummy text Dummy text Dummy text Dummy text Dummy text Dummy text Dummy text Dummy text Dummy text Dummy text</p>
    <div class="image-slot slot-wide" role="img" aria-label="Image placeholder"></div>
  </section>

  <div class="caption caption-cover">Manual Cover Page</div>
  <div class="caption caption-inside">Inside Page look</div>
</body>
</html>
```